Cover for "TANDEM! The skill and rhythm of guiding teams through calm and delight"

My first book for a global audience of modern performance leaders needs its cover!
I am an international executive coach and I've developed a new approach to replace classic Performance Management with a natural, sustainable approach fit for human beings :) My first book is about this approach and serves two purposes: helping leaders and sparking their curiosity to learn more, and positioning myself as a thought leader in the field.
The book is built on personal experience; it is both professional and personal ("From me to You"), and I'd like to position it beyond classic categorisation.
Its cover should communicate humanness, naturalness, ease and joy, within an unmistakably business-y context. I would like to see designs that use the color yellow (but not sure it communicates the right things).
Updates

Sick

Target Market(s)

Leaders who aspire to have a positive impact and deliver results in a meaningful way

Industry/Entity Type

Consulting & Executive Coaching - Trusted Advisor

Font styles to use
Other font styles liked:
• Helvetica Neue

Colors
0094D4
00A9DD
6FCCEA
C7EBF8
E9F6FB
FFC000
F8CF3A
FAE287
FDF2CF
FEFAEE
EE7325
F08F49
F5BC92
FAE3D3
FDF4ED

Requirements
Must have
• A both-and feeling to it (see description), e.g., masculine AND feminine, business AND humanness. Power with, not power over...
Should not have
• Too much "bling" - no classic status symbol business success language

```html
<!DOCTYPE html>
<html lang="en">
<head>
<meta charset="utf-8">
<title>TANDEM! – Book Cover</title>
<link href="https://fonts.googleapis.com/css2?family=Arimo:ital,wght@0,700;1,700&display=swap" rel="stylesheet">
<style>
  :root {
    --backdrop: #ffffff;
    --yellow-top: #fcc200;
    --yellow-bottom: #dba704;
    --ink: #2a2a2a;
    --accent: #fcc000;
    --piece-dark: #3a2518;
    --piece-mid: #6b4a2e;
    --crown-gold: #d8c38a;
  }
  * { margin: 0; padding: 0; box-sizing: border-box; }
  html, body {
    width: 1200px; height: 1200px; overflow: hidden;
    background: var(--backdrop);
  }
  .canvas { position: relative; width: 1200px; height: 1200px; }
  .cover {
    position: absolute; left: 255px; top: 83px;
    width: 690px; height: 1034px; overflow: hidden;
    background: linear-gradient(180deg, var(--yellow-top) 0%, var(--yellow-bottom) 100%);
    font-family: "Arimo", "Helvetica Neue", Arial, sans-serif;
    color: var(--ink);
  }
  .title { font-size: inherit; }
  .title-letter {
    position: absolute; z-index: 2; font-weight: 700;
    font-size: 160px; line-height: 1;
    width: 140px; text-align: center;
  }
  .col-left { left: 180px; }
  .col-right { left: 382px; }
  .slash-lines { position: absolute; inset: 0; z-index: 3; pointer-events: none; }
  .chess-piece {
    position: absolute; z-index: 1; left: 192px; top: 594px; width: 117px; height: 303px;
    background: linear-gradient(180deg, var(--crown-gold) 0%, var(--crown-gold) 26%, var(--piece-mid) 30%, var(--piece-dark) 100%);
    border-radius: 36px 36px 12px 12px;
  }
  .subtitle-band {
    position: absolute; left: 279px; top: 696px; width: 411px; height: 170px;
    background: var(--ink);
  }
  .subtitle-rule {
    position: absolute; left: 66px; top: 18px; width: 4px; height: 135px;
    background: var(--accent);
  }
  .subtitle {
    position: absolute; left: 85px; top: 28px;
    color: var(--accent); font-style: italic; font-weight: 700;
    font-size: 22px; line-height: 29px; text-transform: uppercase;
    letter-spacing: -0.3px; white-space: nowrap;
  }
  .author-name {
    position: absolute; left: 0; right: 0; top: 954px;
    text-align: center; font-weight: 700; font-size: 39px;
    letter-spacing: 4px; line-height: 1;
  }
</style>
</head>
<body>
<div class="canvas">
  <section class="cover">
    <h1 class="title" aria-label="TANDEM!">
      <span class="title-letter col-left" style="top:23px">T</span>
      <span class="title-letter col-right" style="top:90px">A</span>
      <span class="title-letter col-left" style="top:157px">N</span>
      <span class="title-letter col-right" style="top:224px">D</span>
      <span class="title-letter col-left" style="top:291px">E</span>
      <span class="title-letter col-right" style="top:358px">M</span>
      <span class="title-letter col-left" style="top:425px">!</span>
    </h1>
    <svg class="slash-lines" width="690" height="1034" viewBox="0 0 690 1034" aria-hidden="true">
      <line x1="382" y1="70" x2="159" y2="367" stroke="#2a2a2a" stroke-width="1.2"/>
      <line x1="589" y1="356" x2="365" y2="654" stroke="#2a2a2a" stroke-width="1.2"/>
    </svg>
    <div class="subtitle-band">
      <div class="subtitle-rule"></div>
      <p class="subtitle">The skill and rhythm<br>of guiding teams<br>through calm<br>and delight</p>
    </div>
    <div class="chess-piece" role="img" aria-label="Photo of a dark wooden chess pawn wearing a small gold crown"></div>
    <p class="author-name">AUTHOR NAME</p>
  </section>
</div>
</body>
</html>
```